Picture Ads

We need some banner ads for our home business opportunity, we are evolving from text to picture ads. I have added some examples of what other distributors are using. We are looking for something really eye catching with some good key words and nice bright colours and to include our photo (attached)
Key words to include:
Booming online business
Personal Development and Leadership Industry
Earn an executive income from home
Simple 3 step system
Make up to $5,000 per sale
Not MLM
The size needs to be: 1000 x 35 pixels
13.9 x 4.75 Inches
35.3 x 11.1 cm
I think different platforms accept different sizes, not too familiar with it yet, any guidance welcome. I've clicked project for 2 days if that is to prioritise the order?
Many thanks,
Maren

Industry/Entity Type

Business

```html
<!DOCTYPE html>
<html lang="en">
<head>
<meta charset="utf-8">
<title>Booming Online Business Banner</title>
<link href="https://fonts.googleapis.com/css2?family=Bebas+Neue&family=Open+Sans:wght@400;600&family=Patrick+Hand&display=swap" rel="stylesheet">
<style>
  :root {
    --bg-deep: #0a5fb4;
    --bg-mid: #1a8de0;
    --bg-light: #4fc3f7;
    --title-hi: #ffffff;
    --title-lo: #8d99a6;
    --title-edge: #2c3e50;
    --subtitle: #ffe14a;
    --copy: #ffffff;
    --money: #39e34a;
    --tick: #8cc63f;
    --cross: #e53935;
    --arrow-hi: #ff3b2f;
    --arrow-lo: #b50d0d;
    --btn-hi: #ffc21a;
    --btn-lo: #f28a00;
    --btn-edge: #d96f00;
    --frame: #ffffff;
    --caption: #222222;
  }
  * { margin: 0; padding: 0; box-sizing: border-box; }
  html, body { width: 1200px; height: 410px; overflow: hidden; background: #ffffff; }

  .banner {
    position: relative;
    width: 1200px;
    height: 410px;
    overflow: hidden;
    background: linear-gradient(135deg, var(--bg-mid) 0%, var(--bg-deep) 55%, var(--bg-mid) 100%);
  }
  .banner__swoosh { position: absolute; inset: 0; }

  .headline {
    position: absolute;
    left: 30px;
    top: 22px;
    font-family: "Bebas Neue", "Arial Narrow", sans-serif;
    font-size: 96px;
    line-height: 1;
    letter-spacing: 3px;
    background: linear-gradient(180deg, var(--title-hi) 0%, #dfe6ec 45%, var(--title-lo) 55%, #e9eef2 100%);
    -webkit-background-clip: text;
    background-clip: text;
    color: transparent;
    -webkit-text-stroke: 1.5px var(--title-edge);
    filter: drop-shadow(0 3px 3px rgba(0, 0, 0, 0.45));
  }

  .divider {
    position: absolute;
    left: 30px;
    top: 116px;
    width: 918px;
    height: 9px;
    background: repeating-linear-gradient(-60deg, rgba(255,255,255,0.85) 0 3px, transparent 3px 8px);
  }

  .subtitle {
    position: absolute;
    left: 30px;
    top: 154px;
    font-family: "Open Sans", Arial, sans-serif;
    font-size: 36px;
    color: var(--subtitle);
    text-shadow: 0 2px 3px rgba(0, 0, 0, 0.35);
    white-space: nowrap;
  }

  .benefits {
    position: absolute;
    left: 32px;
    top: 205px;
    list-style: none;
    font-family: "Open Sans", Arial, sans-serif;
    font-size: 36px;
    line-height: 50px;
    color: var(--copy);
    text-shadow: 0 2px 3px rgba(0, 0, 0, 0.35);
  }
  .benefits__item { display: flex; align-items: center; gap: 10px; white-space: nowrap; }
  .benefits__icon { width: 32px; height: 32px; flex: none; }
  .benefits__money { color: var(--money); font-weight: 600; }

  .growth-arrow { position: absolute; left: 958px; top: -4px; width: 112px; height: 102px; }

  .snapshot {
    position: absolute;
    left: 984px;
    top: 50px;
    width: 198px;
    height: 248px;
    padding: 10px 10px 0;
    background: var(--frame);
    transform: rotate(2deg);
    box-shadow: 0 4px 10px rgba(0, 0, 0, 0.4);
  }
  .snapshot__photo {
    width: 178px;
    height: 200px;
    background: linear-gradient(160deg, #6b4a3a 0%, #c98f6e 45%, #e8b48a 70%, #7a4e30 100%);
  }
  .snapshot__caption {
    font-family: "Patrick Hand", "Comic Sans MS", cursive;
    font-size: 16px;
    color: var(--caption);
    text-align: center;
    margin-top: 6px;
    white-space: nowrap;
  }

  .cta {
    position: absolute;
    left: 914px;
    top: 318px;
    width: 262px;
    height: 76px;
    display: flex;
    align-items: center;
    border-radius: 8px;
    border: 2px solid var(--btn-edge);
    background: linear-gradient(180deg, var(--btn-hi) 0%, var(--btn-lo) 100%);
    box-shadow: 0 4px 8px rgba(0, 0, 0, 0.35);
    text-decoration: none;
  }
  .cta__label {
    flex: 1;
    text-align: center;
    font-family: "Bebas Neue", "Arial Narrow", sans-serif;
    font-size: 46px;
    letter-spacing: 1px;
    color: #ffffff;
    text-shadow: 0 2px 2px rgba(150, 70, 0, 0.7);
    padding-top: 4px;
  }
  .cta__chevron {
    width: 58px;
    height: 100%;
    display: flex;
    align-items: center;
    justify-content: center;
    border-left: 2px solid rgba(255, 255, 255, 0.45);
  }
</style>
</head>
<body>
<main class="banner">
  <svg class="banner__swoosh" viewBox="0 0 1200 410" preserveAspectRatio="none" aria-hidden="true">
    <defs>
      <linearGradient id="swoosh-light" x1="0" y1="0" x2="1" y2="0">
        <stop offset="0" stop-color="#8fe0ff" stop-opacity="0"/>
        <stop offset="0.6" stop-color="#8fe0ff" stop-opacity="0.35"/>
        <stop offset="1" stop-color="#bdf0ff" stop-opacity="0.5"/>
      </linearGradient>
    </defs>
    <path d="M0 300 C 300 180, 700 120, 1200 40 L1200 0 L0 0 Z" fill="#000" opacity="0.06"/>
    <path d="M200 410 C 500 250, 850 190, 1200 170 L1200 410 Z" fill="url(#swoosh-light)"/>
    <path d="M0 240 C 350 170, 800 120, 1200 20" stroke="#bdf0ff" stroke-opacity="0.3" stroke-width="3" fill="none"/>
    <path d="M400 410 C 650 300, 950 250, 1200 240" stroke="#ffffff" stroke-opacity="0.25" stroke-width="2" fill="none"/>
  </svg>

  <h1 class="headline">Booming Online Business</h1>
  <div class="divider"></div>
  <p class="subtitle">Personal Development and Leadership Industry</p>

  <ul class="benefits">
    <li class="benefits__item">
      <svg class="benefits__icon" viewBox="0 0 32 32"><path d="M4 17 L12 25 L28 6" stroke="var(--tick)" stroke-width="5" fill="none" stroke-linecap="round" stroke-linejoin="round"/></svg>
      Earn an executive income from home
    </li>
    <li class="benefits__item">
      <svg class="benefits__icon" viewBox="0 0 32 32"><path d="M4 17 L12 25 L28 6" stroke="var(--tick)" stroke-width="5" fill="none" stroke-linecap="round" stroke-linejoin="round"/></svg>
      Simple 3 step system
    </li>
    <li class="benefits__item">
      <svg class="benefits__icon" viewBox="0 0 32 32"><path d="M4 17 L12 25 L28 6" stroke="var(--tick)" stroke-width="5" fill="none" stroke-linecap="round" stroke-linejoin="round"/></svg>
      <span>Make up to <span class="benefits__money">$5,000</span> per sale</span>
    </li>
    <li class="benefits__item">
      <svg class="benefits__icon" viewBox="0 0 32 32"><path d="M7 7 L25 25 M25 7 L7 25" stroke="var(--cross)" stroke-width="5" fill="none" stroke-linecap="round"/></svg>
      Not MLM
    </li>
  </ul>

  <svg class="growth-arrow" viewBox="0 0 112 102" aria-hidden="true">
    <defs>
      <linearGradient id="arrow-fill" x1="0" y1="1" x2="1" y2="0">
        <stop offset="0" stop-color="var(--arrow-lo)"/>
        <stop offset="1" stop-color="var(--arrow-hi)"/>
      </linearGradient>
    </defs>
    <path d="M6 100 L30 100 L56 58 L66 72 L94 8 L60 24 L72 32 L52 62 L40 46 Z" fill="url(#arrow-fill)" stroke="#7a0000" stroke-width="1.5"/>
  </svg>

  <figure class="snapshot">
    <div class="snapshot__photo" role="img" aria-label="Portrait photo of Maren and Ysolde Harrow"></div>
    <figcaption class="snapshot__caption">Maren and Ysolde Harrow</figcaption>
  </figure>

  <a class="cta" href="#">
    <span class="cta__label">Get Started</span>
    <span class="cta__chevron">
      <svg width="26" height="34" viewBox="0 0 26 34" aria-hidden="true"><path d="M4 3 L20 17 L4 31" stroke="#ffffff" stroke-width="6" fill="none" stroke-linejoin="round"/></svg>
    </span>
  </a>
</main>
</body>
</html>
```